Business Cards

Need business card design that I can update for new employees and details. Needs to incorporate our logo, be bright and fun (in line with tourism and holidays)
Would like a Map of Western Australia on the front with locations all the caravan parks we own (just purchased Tom Price so please include that as well as others listed on our website).
Target Market(s)
Famillies
Contact Information for Business Card
5 Cards -
Mark Pettigrew (Director) e: pettigrew@bluewattle.com.au p: 0462 318 904
Lucy Pettigrew (Director) e: pettigrew@bluewattle.com.au p: 0455 896 320
Peter Halvorsen (General Manager) e: halvorsen@bluewattle.com.au p: 0471 552 648
Mina Halvorsen (General Manager) e: halvorsen@bluewattle.com.au p: 0471 552 649
Neil Whitcombe (Training and Operations Manager) - e: whitcombe@bluewattle.com.au p:0427 160 493
Colors
Designer to choose colors to be used in the design.
Look and feel
Each slider illustrates characteristics of the customer's brand and the style your logo design should communicate.

```html
<!DOCTYPE html>
<html lang="en">
<head>
<meta charset="utf-8">
<title>Bluewattle Tourist Parks – Business Card</title>
<link rel="stylesheet" href="https://fonts.googleapis.com/css2?family=Roboto:wght@400;500&amp;family=Roboto+Condensed:wght@500&amp;display=swap">
<style>
  :root {
    --backdrop: #2b2b2b;
    --paper: #f1f1f1;
    --teal: #3db8c1;
    --teal-soft: #5db6b1;
    --ink: #454545;
    --rule: #8a8a8a;
    --white: #ffffff;
  }
  * { margin: 0; padding: 0; box-sizing: border-box; }
  html, body {
    width: 1200px; height: 960px; overflow: hidden;
    background: var(--backdrop);
    font-family: "Roboto", Arial, sans-serif;
  }
  .card {
    position: absolute;
    width: 600px; height: 343px;
    box-shadow: 0 3px 8px rgba(0,0,0,.45);
  }
  .card--front { left: 314px; top: 113px; background: var(--paper); }
  .card--back  { left: 311px; top: 472px; background: var(--teal); }

  /* brand block */
  .brand { position: absolute; text-align: center; }
  .brand__mark { display: block; margin: 0 auto; }
  .brand__name, .brand__tagline {
    display: block;
    font-weight: 400;
    text-transform: uppercase;
    line-height: 1;
    white-space: nowrap;
  }
  .card--front .brand { left: 310px; top: 41px; width: 270px; }
  .card--front .brand__mark { width: 70px; height: 70px; background: var(--teal); opacity: .85; }
  .card--front .brand__name { color: var(--ink); font-size: 29px; letter-spacing: 3.5px; margin-top: 2px; }
  .card--front .brand__tagline { color: var(--ink); font-size: 13px; letter-spacing: 3.6px; margin-top: 5px; }

  .card--back .brand { left: 130px; top: 100px; width: 340px; }
  .card--back .brand__mark { width: 91px; height: 91px; border: 3px solid var(--white); }
  .card--back .brand__name { color: var(--white); font-size: 37px; letter-spacing: 5px; margin-top: 3px; }
  .card--back .brand__tagline { color: var(--white); font-size: 16px; letter-spacing: 4.8px; margin-top: 8px; }

  /* person */
  .tab { position: absolute; left: 0; top: 190px; width: 13px; height: 40px; background: var(--teal); }
  .person { position: absolute; left: 43px; top: 186px; }
  .person__name {
    font-family: "Roboto Condensed", "Arial Narrow", sans-serif;
    font-weight: 500; font-size: 22px; color: var(--teal);
    text-transform: uppercase; line-height: 1.1;
  }
  .person__role { font-size: 16px; color: var(--teal-soft); text-transform: uppercase; margin-top: 3px; margin-left: 1px; }
  .divider { position: absolute; left: 44px; top: 241px; width: 515px; height: 1px; background: var(--rule); }

  .contact { position: absolute; left: 43px; top: 252px; list-style: none; }
  .contact__item {
    display: flex; align-items: center; gap: 8px;
    font-size: 14.5px; color: var(--ink); height: 19px;
  }
  .contact__item svg { width: 13px; height: 13px; fill: var(--teal); flex: none; }

  .back-url {
    position: absolute; left: 0; right: 0; top: 293px;
    text-align: center; color: var(--white);
    font-size: 14.5px; letter-spacing: 3.2px;
  }
</style>
</head>
<body>

<section class="card card--front">
  <div class="brand">
    <span class="brand__mark"></span>
    <span class="brand__name">Bluewattle</span>
    <span class="brand__tagline">Tourist Parks</span>
  </div>

  <span class="tab"></span>
  <div class="person">
    <h1 class="person__name">Mark Pettigrew</h1>
    <p class="person__role">Director</p>
  </div>
  <span class="divider"></span>

  <ul class="contact">
    <li class="contact__item">
      <svg viewBox="0 0 24 24"><path d="M6.6 10.8a15.1 15.1 0 0 0 6.6 6.6l2.2-2.2c.3-.3.7-.4 1-.2 1.1.4 2.3.6 3.6.6.6 0 1 .4 1 1V20c0 .6-.4 1-1 1A17 17 0 0 1 3 4c0-.6.4-1 1-1h3.5c.6 0 1 .4 1 1 0 1.2.2 2.4.6 3.6.1.3 0 .7-.2 1z"/></svg>
      0462 318 904
    </li>
    <li class="contact__item">
      <svg viewBox="0 0 24 24"><path d="M2 5h20v14H2zm2 2v.5l8 5 8-5V7l-8 5z"/></svg>
      pettigrew@bluewattle.com.au
    </li>
    <li class="contact__item">
      <svg viewBox="0 0 24 24"><path d="M12 2a10 10 0 1 0 0 20 10 10 0 0 0 0-20zm-1 17.9A8 8 0 0 1 4.2 10L9 14.8v1a2 2 0 0 0 2 2zm6.9-2.5A2 2 0 0 0 16 16h-1v-3a1 1 0 0 0-1-1H8v-2h2a1 1 0 0 0 1-1V7h2a2 2 0 0 0 2-2v-.4a8 8 0 0 1 2.9 12.8z"/></svg>
      www.bluewattle.com.au
    </li>
  </ul>
</section>

<section class="card card--back">
  <div class="brand">
    <span class="brand__mark"></span>
    <span class="brand__name">Bluewattle</span>
    <span class="brand__tagline">Tourist Parks</span>
  </div>
  <p class="back-url">www.bluewattle.com.au</p>
</section>

</body>
</html>
```